Sign listing benefits of Wash and Fold Service

Sign 48 inches wide and 24 inches height to showcase service listed above.
Benefits include:
Saves Money
Saves Time
Convenient
Stain Treatment

Looking for something colorful (Blue and white are our business colors) the look of a laundromat business.

```html
<!DOCTYPE html>
<html lang="en">
<head>
<meta charset="UTF-8">
<title>Wash and Fold Benefits Sign</title>
<link rel="stylesheet" href="https://fonts.googleapis.com/css2?family=Archivo+Black&display=swap">
<style>
  :root {
    --page-bg: #e9e9e9;
    --sign-white: #ffffff;
    --laundry-blue: #0f9de2;
    --laundry-blue-deep: #0a8fd6;
    --navy: #2e3a8f;
    --cyan: #22b8ee;
    --bubble-light: #d9f4fd;
    --bubble-edge: #9fe0f7;
  }
  html, body {
    margin: 0;
    padding: 0;
    width: 1200px;
    height: 778px;
    overflow: hidden;
    background: var(--page-bg);
  }
  .sign {
    position: absolute;
    left: 0;
    top: 89px;
    width: 1200px;
    height: 600px;
    display: block;
  }
  .benefit-text {
    font-family: "Archivo Black", "Arial Black", sans-serif;
    font-size: 100px;
  }
  .benefit-shadow { fill: var(--navy); stroke: var(--navy); stroke-width: 14px; stroke-linejoin: round; }
  .benefit-outer { fill: var(--cyan); stroke: var(--cyan); stroke-width: 14px; stroke-linejoin: round; }
  .benefit-inner { fill: var(--navy); stroke: var(--sign-white); stroke-width: 6px; stroke-linejoin: round; paint-order: stroke; }
  .icon-badge { fill: var(--bubble-light); stroke: var(--sign-white); stroke-width: 4px; }
</style>
</head>
<body>
<svg class="sign" viewBox="0 0 1200 600" xmlns="http://www.w3.org/2000/svg" aria-label="Wash and fold service benefits sign">
  <defs>
    <radialGradient id="bubble-field" cx="70%" cy="45%" r="60%">
      <stop offset="0%" stop-color="#ffffff"/>
      <stop offset="100%" stop-color="#eefafe"/>
    </radialGradient>
    <g id="benefit-money"><text class="benefit-text" x="143" y="139" textLength="775" lengthAdjust="spacingAndGlyphs">SAVES MONEY</text></g>
    <g id="benefit-time"><text class="benefit-text" x="143" y="272" textLength="641" lengthAdjust="spacingAndGlyphs">SAVES TIME</text></g>
    <g id="benefit-convenient"><text class="benefit-text" x="143" y="406" textLength="696" lengthAdjust="spacingAndGlyphs">CONVENIENT</text></g>
    <g id="benefit-stain"><text class="benefit-text" x="143" y="535" textLength="992" lengthAdjust="spacingAndGlyphs">STAIN TREATMENT</text></g>
  </defs>

  <rect class="sign-base" width="1200" height="600" fill="var(--sign-white)"/>
  <rect class="bubble-area" x="560" y="0" width="640" height="600" fill="url(#bubble-field)" role="img" aria-label="Floating soap bubbles"/>

  <path class="blue-panel" d="M0 0 H615 C565 120 600 210 560 300 C520 400 585 480 640 600 H0 Z" fill="var(--laundry-blue)" role="img" aria-label="Blue tiled laundromat wall with soap foam edge"/>
  <path class="foam-edge" d="M615 0 C565 120 600 210 560 300 C520 400 585 480 640 600" fill="none" stroke="var(--bubble-edge)" stroke-width="8"/>

  <g class="icon-badges">
    <circle class="icon-badge" cx="73" cy="100" r="45" role="img" aria-label="Piggy bank icon"/>
    <circle class="icon-badge" cx="73" cy="233" r="45" role="img" aria-label="Clock in hand icon"/>
    <circle class="icon-badge" cx="73" cy="362" r="45" role="img" aria-label="Thumbs up icon"/>
    <circle class="icon-badge" cx="73" cy="496" r="45" role="img" aria-label="Stained shirt icon"/>
  </g>

  <g class="benefit-layer benefit-shadow" transform="translate(7 8)">
    <use href="#benefit-money"/><use href="#benefit-time"/><use href="#benefit-convenient"/><use href="#benefit-stain"/>
  </g>
  <g class="benefit-layer benefit-outer">
    <use href="#benefit-money"/><use href="#benefit-time"/><use href="#benefit-convenient"/><use href="#benefit-stain"/>
  </g>
  <g class="benefit-layer benefit-inner">
    <use href="#benefit-money"/><use href="#benefit-time"/><use href="#benefit-convenient"/><use href="#benefit-stain"/>
  </g>
</svg>
</body>
</html>
```